Website for the new investment company.

We are building a website for a new company. This will be an investment company. The name of the company is Birch Harbor Capital, or BHC. We don't have a company logo yet, so happy to take suggestions on that as well (and will add that to the final cost). The investors of this company will exclusively be Dunmore College alumni graduates. The investors are not students, but instead older professionals in various industries, that previously graduated from the Dunmore College. This company will establish an investment fund and invest in multiple businesses.
The purpose of the website will be to educate Dunmore alumni on the investment fund.
We are looking for:
1. The design to be relatable, but not the copy of the Dunmore College website. https://www.dunmorecollege-example.edu/
2. This is an investment website and must mimic other similar websites
https://quillmark-funds.com/
https://www.tallowvane.com/
https://brevinholt-group.com/site/global/home/p_home.gsp
3. Project timeline. We are focused on receiving a design in the next two weeks and then finishing the website over the following 2 weeks. We anticipate paying for additional work and customization after the designs are provided.
4. Website Pages:
1) Homepage - Mission and Objective (high quality photos along with text that we will provide after selecting the winning design)
2) Background - Text and biographies on the 2 founders (high quality photos along with text that we will provide after selecting the winning design)
3) Advisory Board - Text and biographies on the investment Fund's 3 advisory board members (high quality photos along with text that we will provide after selecting the winning design)
4) Fund I - Text and information on the specific investment fund including pictures and biographies of the investment committee (high quality photos along with text that we will provide after selecting the winning design)
5) Contact Us - Typical website contact page for visitors

Target Market(s)

Dunmore Alumni graduates

Industry/Entity Type

Investment

Coding

Coded - Design and coding required

Font styles to use
Serif
Sans Serif

Colors
0054AA
0677BA
7BADD7
CADEEF
E8F1F8

Requirements
Must have
• Must look like other private investment websites as provided in project description
Nice to have
• Mimics the Dunmore College style, but definitely needs to be different. This company has no direct relationship with Dunmore College.
Should not have
• No commercial transactions, no credit card payments etc. Do not replicate any logos, designs or proprietary content from Dunmore College.

```html
<!DOCTYPE html>
<html lang="en">
<head>
<meta charset="utf-8">
<title>Birch Harbor Capital</title>
<link rel="stylesheet" href="https://fonts.googleapis.com/css2?family=Oswald:wght@300;400;500&family=Poppins:ital,wght@0,400;0,500;0,600;0,700;1,400&display=swap">
<style>
:root{
  --navy:#0c2352;
  --navy-deep:#0a1d44;
  --blue:#0054AA;
  --sky:#0677BA;
  --mist:#CADEEF;
  --ice:#E8F1F8;
  --grey-band:#f3f3f4;
  --ink:#1b1b1f;
  --muted:#4a4a55;
  --white:#ffffff;
  --star:#f5b400;
}
*{margin:0;padding:0;box-sizing:border-box}
html,body{width:1200px;height:4888px;overflow:hidden}
body{font-family:"Poppins",sans-serif;color:var(--ink);background:var(--white);position:relative}
section,header,footer{position:relative;width:1200px;overflow:hidden}
.photo{position:absolute;overflow:hidden}
.heading{font-family:"Oswald",sans-serif;font-weight:400;color:var(--navy);letter-spacing:1px;text-transform:uppercase}
.heading-center{position:absolute;left:0;width:1200px;display:flex;justify-content:center;align-items:center;gap:26px;font-size:46px}
.heading-center::before,.heading-center::after{content:"";width:110px;height:3px;background:var(--navy)}
.heading-right{display:flex;align-items:center;gap:22px;font-size:42px;white-space:nowrap}
.heading-right::after{content:"";width:100px;height:3px;background:var(--navy)}
.body-text{font-size:14px;line-height:1.6;color:var(--ink);text-align:justify}
.btn{display:inline-flex;align-items:center;justify-content:center;background:var(--navy);color:var(--white);font-size:12px;font-weight:600;border-radius:20px;text-transform:uppercase;letter-spacing:.5px}

/* header */
.site-header{height:112px;background:var(--white)}
.brand{position:absolute;left:70px;top:38px;display:flex;align-items:center;gap:12px;font-weight:700;font-size:24px;color:var(--navy);text-transform:uppercase;letter-spacing:.3px;white-space:nowrap}
.brand-mark{width:30px;height:30px;background:var(--navy);flex:none}
.main-nav{position:absolute;right:70px;top:44px;display:flex;gap:30px;font-size:15px;color:var(--navy);white-space:nowrap}
.main-nav .active{border-bottom:2px solid var(--navy);padding-bottom:6px}

/* hero */
.hero{height:620px}
.hero-photo{left:0;top:0;width:1200px;height:620px;background:linear-gradient(100deg,#0d2a5e 0%,#1a3a6c 38%,#5c6f86 62%,#9aa0a6 80%,#6b6660 100%)}
.hero-shade{position:absolute;left:0;top:0;width:700px;height:620px;background:linear-gradient(90deg,rgba(8,26,66,.85),rgba(8,26,66,0))}
.hero-title{position:absolute;left:78px;top:170px;font-weight:700;font-size:50px;color:var(--white);text-transform:uppercase;white-space:nowrap}
.hero-text{position:absolute;left:78px;top:250px;width:470px;font-size:17px;line-height:1.55;color:var(--white)}
.hero .btn{position:absolute;left:78px;top:384px;width:190px;height:54px;background:var(--white);color:var(--navy);border-radius:27px;font-size:14px}
.dots{position:absolute;display:flex;gap:12px;align-items:center}
.dot{width:16px;height:5px;background:rgba(255,255,255,.45)}
.dot.on{width:30px;background:var(--white)}

/* mission */
.mission{height:668px}
.mission-frame{position:absolute;left:100px;top:150px;width:400px;height:420px;background:var(--navy);border-radius:0 0 0 34px}
.mission-photo{left:130px;top:108px;width:380px;height:440px;border-radius:0 40px 0 40px;background:linear-gradient(135deg,#c9cdd3,#8f99a8 50%,#4c5a73)}
.mission .heading-right{position:absolute;left:578px;top:172px}
.mission .body-text{position:absolute;left:578px;top:252px;width:510px}
.mission .btn{position:absolute;left:578px;top:452px;width:136px;height:38px}

/* founders */
.founders{height:740px;background:var(--grey-band)}
.founders .heading-center{top:108px}
.founders-intro{position:absolute;left:170px;top:216px;width:860px;font-size:15px;line-height:1.65;text-align:center}
.founder-card{position:absolute;top:330px;width:518px;height:292px;background:var(--white);border-radius:0 50px 0 50px;box-shadow:0 6px 18px rgba(0,0,0,.12)}
.founder-photo{left:16px;top:16px;width:216px;height:260px;border-radius:0 40px 0 40px;background:linear-gradient(160deg,#d7dade,#a7afb9 60%,#3b4352)}
.founder-name{position:absolute;left:252px;top:40px;font-size:26px;font-weight:500;color:var(--navy)}
.founder-role{position:absolute;left:252px;top:80px;font-size:16px;color:var(--blue)}
.founder-bio{position:absolute;left:252px;top:112px;width:244px;font-size:14px;line-height:1.6;text-align:justify}
.social{position:absolute;display:flex;gap:10px}
.social .sq{width:26px;height:26px;background:var(--navy);border-radius:4px}
.social .ci{width:26px;height:26px;background:var(--navy);border-radius:50%}

/* advisory */
.advisory{height:800px}
.advisory .heading-center{top:128px}
.advisor-card{position:absolute;top:236px;width:316px;height:452px;background:var(--white);box-shadow:0 6px 18px rgba(0,0,0,.13);border-radius:0 50px 0 50px;text-align:center}
.advisor-photo{left:14px;top:14px;width:288px;height:216px;border-radius:40px 0 0 0;background:linear-gradient(160deg,#b8bcc2,#6d7480 55%,#2c333f)}
.advisor-name{position:absolute;left:0;width:100%;top:258px;font-size:22px;font-weight:500}
.advisor-bio{position:absolute;left:33px;width:250px;top:300px;font-size:14px;line-height:1.55}
.advisor-card .btn{position:absolute;left:94px;top:372px;width:128px;height:32px;font-size:11px}

/* fund */
.fund{height:652px;background:var(--grey-band)}
.fund .heading-right{position:absolute;left:124px;top:186px}
.fund .body-text{position:absolute;left:124px;top:266px;width:520px}
.fund .btn{position:absolute;left:124px;top:470px;width:136px;height:40px}
.fund-frame{position:absolute;left:700px;top:150px;width:390px;height:400px;background:var(--navy);border-radius:0 0 34px 0}
.fund-photo{left:672px;top:100px;width:400px;height:420px;border-radius:40px 0 40px 0;background:linear-gradient(135deg,#e5e6e3,#c3c8cc 50%,#7f8893)}

/* stats */
.stats{height:248px;background:linear-gradient(90deg,#0a2150,#122c60 60%,#0a2150)}
.stat{position:absolute;top:66px;color:var(--white)}
.stat-num{font-size:52px;font-weight:500;line-height:1}
.stat-line{width:220px;height:1px;background:rgba(255,255,255,.55);margin:18px 0 14px}
.stat-label{font-size:16px;line-height:1.3}

/* testimonials */
.testimonials{height:692px}
.testimonials .heading-center{top:138px}
.quote-card{position:absolute;top:248px;width:334px;height:172px;background:var(--white);box-shadow:0 6px 18px rgba(0,0,0,.12);padding:26px 22px;font-size:14px;font-style:italic;line-height:1.55;text-align:center}
.reviewer{position:absolute;top:460px;display:flex;align-items:center;gap:14px}
.avatar{width:58px;height:58px;border-radius:50%;background:linear-gradient(160deg,#c8c2bb,#7b6f66)}
.reviewer-name{font-size:15px;font-weight:600;color:var(--navy)}
.reviewer-role{font-size:12px;color:var(--muted)}
.stars{display:flex;gap:2px;margin-top:2px}
.testimonials .dot{background:#c5cad3}
.testimonials .dot.on{background:var(--navy)}

/* footer */
.site-footer{height:356px;background:var(--navy-deep);color:var(--white)}
.footer-title{position:absolute;top:84px;font-size:17px;font-weight:600;text-transform:uppercase}
.footer-title::after{content:"";display:block;width:44px;height:2px;background:var(--white);margin-top:8px}
.quick-links{position:absolute;left:140px;top:134px;list-style:none;font-size:14px;line-height:2}
.quick-links li::before{content:"";display:inline-block;width:6px;height:6px;background:var(--white);border-radius:50%;margin-right:12px;vertical-align:middle}
.footer-brand{position:absolute;left:0;width:1200px;top:170px;display:flex;justify-content:center;align-items:center;gap:14px;font-weight:700;font-size:32px;text-transform:uppercase;white-space:nowrap}
.footer-brand .brand-mark{width:36px;height:36px;background:var(--white)}
.footer-social{position:absolute;left:0;width:1200px;top:246px;display:flex;justify-content:center;gap:10px}
.footer-social span{width:26px;height:26px;border:1.5px solid var(--white);border-radius:50%}
.contact-list{position:absolute;left:870px;top:134px;list-style:none;font-size:13px;line-height:1.35}
.contact-list li{display:flex;gap:12px;margin-bottom:16px;align-items:flex-start}
.contact-icon{width:26px;height:26px;border-radius:50%;background:var(--white);flex:none;display:flex;align-items:center;justify-content:center}
.copyright{position:absolute;left:0;bottom:0;width:1200px;height:40px;background:#071633;display:flex;align-items:center;justify-content:center;font-size:13px}
</style>
</head>
<body>

<header class="site-header">
  <div class="brand"><span class="brand-mark"></span>Birch Harbor Capital</div>
  <nav class="main-nav">
    <span class="active">Home</span><span>Founders</span><span>Advisory Board</span><span>Fund Investment</span><span>Contact Us</span>
  </nav>
</header>

<section class="hero">
  <div class="photo hero-photo" role="img" aria-label="Desk with laptop, charts and financial paperwork"></div>
  <div class="hero-shade"></div>
  <h1 class="hero-title">Birch Harbor Capital</h1>
  <p class="hero-text">Lorem ipsum dolor sit amet, consectetur adipiscing elit. Sed ut est sed nulla viverra fringilla. Quisque non lacus iaculis, tincidunt est sed, porta est.</p>
  <span class="btn">Learn More</span>
  <div class="dots" style="left:545px;top:538px"><span class="dot on"></span><span class="dot"></span><span class="dot"></span></div>
</section>

<section class="mission">
  <div class="mission-frame"></div>
  <div class="photo mission-photo" role="img" aria-label="Team meeting in a bright office around a presentation screen"></div>
  <h2 class="heading heading-right">Mission and Objective</h2>
  <p class="body-text">Lorem ipsum dolor sit amet, consectetur adipiscing elit, sed do eiusmod tempor incididunt ut labore et dolore magna aliqua. Ut enim ad minim veniam, quis nostrud exercitation ullamco laboris nisi ut aliquip ex ea commodo consequat. Lorem ipsum dolor sit amet, consectetur adipiscing elit. Sed ut est sed nulla viverra fringilla.</p>
  <span class="btn">Read More</span>
</section>

<section class="founders">
  <h2 class="heading heading-center">Founders</h2>
  <p class="founders-intro">Lorem ipsum dolor sit amet, consectetur adipiscing elit, sed do eiusmod tempor incididunt ut labore et dolore magna aliqua. Ut enim ad minim veniam, quis nostrud exercitation ullamco laboris nisi ut aliquip.</p>

  <article class="founder-card" style="left:80px">
    <div class="photo founder-photo" role="img" aria-label="Portrait of founder Marcus Hale"></div>
    <h3 class="founder-name">Marcus Hale</h3>
    <p class="founder-role">Lorem ipsum dolor</p>
    <p class="founder-bio">Lorem ipsum dolor sit amet, consectetur adipiscing elit, sed do eiusmod tempor.</p>
    <div class="social" style="left:252px;top:232px"><span class="sq"></span><span class="ci"></span></div>
  </article>

  <article class="founder-card" style="left:620px">
    <div class="photo founder-photo" role="img" aria-label="Portrait of founder Adaeze Okoro"></div>
    <h3 class="founder-name">Adaeze Okoro</h3>
    <p class="founder-role">Lorem ipsum dolor</p>
    <p class="founder-bio">Lorem ipsum dolor sit amet, consectetur adipiscing elit, sed do eiusmod tempor.</p>
    <div class="social" style="left:252px;top:232px"><span class="sq"></span><span class="ci"></span></div>
  </article>
</section>

<section class="advisory">
  <h2 class="heading heading-center">Advisory Board</h2>

  <article class="advisor-card" style="left:100px">
    <div class="photo advisor-photo" role="img" aria-label="Portrait of advisor Marcus Hale"></div>
    <h3 class="advisor-name">Marcus Hale</h3>
    <p class="advisor-bio">Lorem ipsum dolor sit amet, consectetur adipiscing elit, sed</p>
    <span class="btn">Read More</span>
  </article>

  <article class="advisor-card" style="left:442px">
    <div class="photo advisor-photo" role="img" aria-label="Portrait of advisor Theo Barrett" style="background:linear-gradient(160deg,#9fb38f,#5f6e5a 50%,#2e3440)"></div>
    <h3 class="advisor-name">Theo Barrett</h3>
    <p class="advisor-bio">Lorem ipsum dolor sit amet, consectetur adipiscing elit, sed</p>
    <span class="btn">Read More</span>
  </article>

  <article class="advisor-card" style="left:784px">
    <div class="photo advisor-photo" role="img" aria-label="Portrait of advisor Rafael Ortiz" style="background:linear-gradient(160deg,#c7b89e,#8a8170 50%,#2f3440)"></div>
    <h3 class="advisor-name">Rafael Ortiz</h3>
    <p class="advisor-bio">Lorem ipsum dolor sit amet, consectetur adipiscing elit, sed</p>
    <span class="btn">Read More</span>
  </article>
</section>

<section class="fund">
  <h2 class="heading heading-right">Fund Investment</h2>
  <p class="body-text">Lorem ipsum dolor sit amet, consectetur adipiscing elit, sed do eiusmod tempor incididunt ut labore et dolore magna aliqua. Ut enim ad minim veniam, quis nostrud exercitation ullamco laboris nisi ut aliquip ex ea commodo consequat. Lorem ipsum dolor sit amet, consectetur adipiscing elit. Sed ut est sed nulla viverra fringilla.</p>
  <span class="btn">Read More</span>
  <div class="fund-frame"></div>
  <div class="photo fund-photo" role="img" aria-label="Laptop screen showing a bar chart of fund performance"></div>
</section>

<section class="stats">
  <div class="stat" style="left:168px"><div class="stat-num">45</div><div class="stat-line"></div><div class="stat-label">Investment Transactions</div></div>
  <div class="stat" style="left:504px"><div class="stat-num">$500+</div><div class="stat-line"></div><div class="stat-label">Million Asset Value</div></div>
  <div class="stat" style="left:800px"><div class="stat-num">22%</div><div class="stat-line"></div><div class="stat-label">Average Annualized Return<br>On Investment</div></div>
</section>

<section class="testimonials">
  <h2 class="heading heading-center">Our Testimonials</h2>

  <blockquote class="quote-card" style="left:72px">Lorem ipsum dolor sit amet, conse ctetuer adipiscing elit. Aenean commodo ligula eget dolor. Aenean massa. Cum sociis natoque per nitibus et magnis</blockquote>
  <blockquote class="quote-card" style="left:433px">Lorem ipsum dolor sit amet, conse ctetuer adipiscing elit. Aenean commodo ligula eget dolor. Aenean massa. Cum sociis natoque per nitibus et magnis</blockquote>
  <blockquote class="quote-card" style="left:794px">Lorem ipsum dolor sit amet, conse ctetuer adipiscing elit. Aenean commodo ligula eget dolor. Aenean massa. Cum sociis natoque per nitibus et magnis</blockquote>

  <div class="reviewer" style="left:140px">
    <div class="avatar" role="img" aria-label="Reviewer portrait"></div>
    <div><div class="reviewer-name">Marcus Hale</div><div class="reviewer-role">Managing Director</div>
      <div class="stars"><svg width="70" height="13" viewBox="0 0 70 13"><g fill="#f5b400"><path id="st" d="M6.5 0l1.9 4.2 4.6.4-3.5 3 1.1 4.5-4.1-2.4-4.1 2.4 1.1-4.5-3.5-3 4.6-.4z"/><use href="#st" x="14"/><use href="#st" x="28"/><use href="#st" x="42"/><use href="#st" x="56"/></g></svg></div>
    </div>
  </div>
  <div class="reviewer" style="left:500px">
    <div class="avatar" role="img" aria-label="Reviewer portrait"></div>
    <div><div class="reviewer-name">Marcus Hale</div><div class="reviewer-role">Managing Director</div>
      <div class="stars"><svg width="70" height="13" viewBox="0 0 70 13"><g fill="#f5b400"><use href="#st"/><use href="#st" x="14"/><use href="#st" x="28"/><use href="#st" x="42"/><use href="#st" x="56"/></g></svg></div>
    </div>
  </div>
  <div class="reviewer" style="left:862px">
    <div class="avatar" role="img" aria-label="Reviewer portrait"></div>
    <div><div class="reviewer-name">Marcus Hale</div><div class="reviewer-role">Managing Director</div>
      <div class="stars"><svg width="70" height="13" viewBox="0 0 70 13"><g fill="#f5b400"><use href="#st"/><use href="#st" x="14"/><use href="#st" x="28"/><use href="#st" x="42"/><use href="#st" x="56"/></g></svg></div>
    </div>
  </div>

  <div class="dots" style="left:550px;top:568px"><span class="dot on"></span><span class="dot"></span><span class="dot"></span><span class="dot"></span></div>
</section>

<footer class="site-footer">
  <div class="footer-title" style="left:140px">Quick Links</div>
  <ul class="quick-links">
    <li>Mission and Objective</li><li>Founders</li><li>Advisory Board</li><li>Fund Investment</li><li>Contact Us</li>
  </ul>

  <div class="footer-brand"><span class="brand-mark"></span>Birch Harbor Capital</div>
  <div class="footer-social"><span></span><span></span><span></span><span></span><span></span></div>

  <div class="footer-title" style="left:870px">Contact Us</div>
  <ul class="contact-list">
    <li><span class="contact-icon"><svg width="14" height="14" viewBox="0 0 24 24"><path fill="#0a1d44" d="M6.6 10.8a15.1 15.1 0 006.6 6.6l2.2-2.2a1 1 0 011-.25 11.4 11.4 0 003.6.57 1 1 0 011 1V20a1 1 0 01-1 1A17 17 0 013 4a1 1 0 011-1h3.5a1 1 0 011 1c0 1.25.2 2.45.57 3.57a1 1 0 01-.25 1z"/></svg></span><span>CALL US<br>(555) 240-1789</span></li>
    <li><span class="contact-icon"><svg width="14" height="14" viewBox="0 0 24 24"><path fill="#0a1d44" d="M2 5h20v14H2zm2 2v.5l8 5 8-5V7l-8 5z"/></svg></span><span>EMAIL US<br>info@birchharborcapital.com</span></li>
    <li><span class="contact-icon"><svg width="14" height="14" viewBox="0 0 24 24"><path fill="#0a1d44" d="M12 2a7 7 0 00-7 7c0 5 7 13 7 13s7-8 7-13a7 7 0 00-7-7zm0 9.5A2.5 2.5 0 1112 6.5a2.5 2.5 0 010 5z"/></svg></span><span>Address line here dummy<br>Address line here</span></li>
  </ul>

  <div class="copyright">Copyright ©2024 – All Rights Reserved by Company name</div>
</footer>

</body>
</html>
```